CORAL DRIFT INN GRAND OPENING

We are the new owners and just finished completely remodeling our property and rooms in January 2017. To attract new customers we are planning a HOTEL GRAND OPENING PARTY on FEBRUARY 16 , 2017. EVENT WILL START WITH A 5:00PM HAPPY HOUR
WE WILL HAVE: LIVE MUSIC, SNACKS & BOOZE
The event will be a LUAU PARTY THEME

Industry/Entity Type

Property

Font styles to use
Sans Serif

Colors
85cae6
3176b5
ee3036
cadf82
fbed22
fece3e

Requirements
Must have
• property address:
• 4927 Marlowe Lane
• Harlow Key, Fl 32814
• COMPANY LOGO

```html
<!DOCTYPE html>
<html lang="en">
<head>
<meta charset="utf-8">
<title>Coral Drift Inn – Grand Opening Party</title>
<link rel="stylesheet" href="https://fonts.googleapis.com/css2?family=Cinzel:wght@400;600&family=Montserrat:wght@800&family=Kaushan+Script&family=Amatic+SC:wght@700&family=Cabin+Condensed:wght@700&family=Pathway+Gothic+One&display=swap">
<style>
  :root {
    --sky-blue: #85cae6;
    --ocean-blue: #3176b5;
    --sun-yellow: #fbed22;
    --gold: #fece3e;
    --cream: #fdf9ec;
    --white: #ffffff;
    --dusk-dark: #5a2330;
  }
  html, body {
    margin: 0;
    padding: 0;
    overflow: hidden;
    background: #ffffff;
  }
  p, h1, h2 { margin: 0; }
  .poster {
    position: relative;
    width: 777px;
    height: 1200px;
    overflow: hidden;
    background: #f6e27a;
  }
  .sunset-scene {
    position: absolute;
    left: 0; top: 230px;
    width: 777px; height: 970px;
    background:
      radial-gradient(ellipse 180px 420px at 70px 420px, rgba(110, 30, 40, .55), transparent 70%),
      radial-gradient(ellipse 160px 360px at 720px 700px, rgba(110, 30, 40, .45), transparent 70%),
      linear-gradient(180deg, #24434f 0%, #3f6a70 18%, #7fa7a0 36%, #c8c590 52%, #eeb56a 66%, #e58b52 80%, #c9505c 92%, #b23a5a 100%);
  }
  .header-band {
    position: absolute;
    left: 0; top: 0;
    width: 777px; height: 300px;
  }
  .frame {
    position: absolute;
    left: 14px; top: 14px;
    width: 746px; height: 1166px;
    border: 1.5px solid rgba(255, 255, 255, .55);
    pointer-events: none;
  }
  .brand {
    position: absolute;
    top: 52px; left: 0; width: 777px;
    text-align: center;
  }
  .brand-mark {
    display: block;
    width: 80px; height: 80px;
    margin: 0 auto 30px;
    border-radius: 50%;
    background: var(--gold);
  }
  .brand-name {
    font-family: "Cinzel", serif;
    font-weight: 600;
    font-size: 40px;
    line-height: 1;
    letter-spacing: 1px;
    color: var(--ocean-blue);
  }
  .party-art {
    position: absolute;
    left: 252px; top: 324px;
    width: 272px; height: 190px;
    background: radial-gradient(ellipse at 50% 60%, rgba(253, 249, 236, .55), rgba(253, 249, 236, .15) 70%, transparent 100%);
    border-radius: 50% 50% 6px 6px / 60% 60% 6px 6px;
  }
  .headline {
    position: absolute;
    left: 0; width: 777px;
    text-align: center;
    font-family: "Montserrat", sans-serif;
    font-weight: 800;
    color: var(--gold);
    line-height: 1;
  }
  .headline-grand { top: 522px; font-size: 60px; letter-spacing: -1px; }
  .headline-opening { top: 580px; font-size: 49px; letter-spacing: -1px; }
  .headline-party {
    position: absolute;
    left: 0; width: 777px; top: 604px;
    text-align: center;
    font-family: "Kaushan Script", cursive;
    font-size: 72px;
    line-height: 1.1;
    color: var(--ocean-blue);
    transform: rotate(-6deg);
  }
  .venue-name {
    position: absolute;
    left: 0; width: 777px; top: 714px;
    text-align: center;
    font-family: "Amatic SC", sans-serif;
    font-weight: 700;
    font-size: 90px;
    line-height: 1;
    color: var(--cream);
    letter-spacing: 4px;
  }
  .date-row {
    position: absolute;
    left: 94px; top: 820px;
    width: 600px; height: 86px;
  }
  .date-day {
    position: absolute;
    left: 0; top: 2px;
    font-family: "Cinzel", serif;
    font-size: 38px;
    line-height: 40px;
    color: var(--cream);
  }
  .date-number {
    position: absolute;
    left: 214px; top: -8px;
    font-family: "Amatic SC", sans-serif;
    font-weight: 700;
    font-size: 96px;
    line-height: 1;
    color: transparent;
    -webkit-text-stroke: 2px var(--ocean-blue);
  }
  .date-divider {
    position: absolute;
    left: 282px; top: 6px;
    height: 76px;
    border-left: 3px dotted var(--cream);
  }
  .happy-hour {
    position: absolute;
    left: 306px; top: 4px;
    font-family: "Kaushan Script", cursive;
    font-size: 28px;
    line-height: 42px;
    color: var(--cream);
  }
  .start-time {
    position: absolute;
    left: 478px; top: -4px;
    font-family: "Amatic SC", sans-serif;
    font-weight: 700;
    font-size: 96px;
    line-height: 1;
    color: transparent;
    -webkit-text-stroke: 2px var(--cream);
  }
  .dotted-rule {
    position: absolute;
    left: 96px; top: 910px;
    width: 600px;
    border-top: 4px dotted rgba(140, 150, 190, .85);
  }
  .offer-rule {
    position: absolute;
    height: 0;
    border-top: 1.5px solid var(--dusk-dark);
  }
  .offer-rule.top { left: 165px; top: 944px; width: 420px; }
  .offer-rule.bottom { left: 215px; top: 1010px; width: 330px; }
  .offer-list {
    position: absolute;
    left: 0; width: 777px; top: 955px;
    text-align: center;
    font-family: "Cabin Condensed", sans-serif;
    font-weight: 700;
    font-size: 34px;
    line-height: 1.1;
    letter-spacing: 2px;
    color: var(--cream);
  }
  .offer-list .star {
    color: var(--ocean-blue);
    font-size: 20px;
    vertical-align: 5px;
    margin: 0 6px;
  }
  .address {
    position: absolute;
    left: 0; width: 777px; top: 1038px;
    text-align: center;
    font-family: "Pathway Gothic One", sans-serif;
    font-size: 45px;
    line-height: 1.1;
    color: var(--ocean-blue);
  }
  .address .sep { margin: 0 22px; font-size: 26px; vertical-align: 8px; }
  .renovation-note {
    position: absolute;
    left: 0; width: 777px; top: 1126px;
    text-align: center;
    font-family: "Pathway Gothic One", sans-serif;
    font-size: 33px;
    line-height: 1.1;
    letter-spacing: 1px;
    color: var(--cream);
  }
</style>
</head>
<body>
<main class="poster">
  <div class="sunset-scene" role="img" aria-label="Blurred tropical sunset sky with palm tree silhouettes"></div>

  <svg class="header-band" viewBox="0 0 777 300" aria-hidden="true">
    <defs>
      <radialGradient id="sunGlow" cx="50%" cy="30%" r="60%">
        <stop offset="0" stop-color="#fffdf0"/>
        <stop offset=".55" stop-color="#f8ec82"/>
        <stop offset="1" stop-color="#f2d92e"/>
      </radialGradient>
      <linearGradient id="waveBlue" x1="0" x2="1">
        <stop offset="0" stop-color="#3176b5"/>
        <stop offset="1" stop-color="#85cae6"/>
      </linearGradient>
    </defs>
    <path d="M0 262 C130 282 300 282 440 266 C560 252 680 246 777 254 V264 C680 256 560 262 440 276 C300 292 130 292 0 272 Z" fill="#ffffff"/>
    <path d="M0 252 C130 272 300 272 440 256 C560 242 680 236 777 244 V258 C680 250 560 256 440 270 C300 286 130 286 0 266 Z" fill="url(#waveBlue)"/>
    <path d="M0 0 H777 V244 C680 236 560 242 440 256 C300 272 130 272 0 252 Z" fill="url(#sunGlow)"/>
  </svg>

  <header class="brand">
    <span class="brand-mark"></span>
    <div class="brand-name">CORAL DRIFT INN</div>
  </header>

  <div class="party-art" role="img" aria-label="Cocktail glass with umbrella between palm trees on a small island"></div>

  <h1 class="headline headline-grand">GRAND</h1>
  <p class="headline headline-opening">OPENING</p>
  <p class="headline-party">Party</p>

  <h2 class="venue-name">CORAL DRIFT INN</h2>

  <section class="date-row">
    <div class="date-day">THURSDAY<br>FEBRUARY</div>
    <div class="date-number">16</div>
    <div class="date-divider"></div>
    <div class="happy-hour">start with a<br>Happy Hour</div>
    <div class="start-time">5PM</div>
  </section>

  <div class="dotted-rule"></div>

  <div class="offer-rule top"></div>
  <p class="offer-list">SNACKS<span class="star">★</span>LIVE MUSIC<span class="star">★</span>BOOZE</p>
  <div class="offer-rule bottom"></div>

  <p class="address">4927 Marlowe Lane<span class="sep">·</span>Harlow Key, Fl 32814</p>

  <p class="renovation-note">PROPERTY HAS RECENTLY BEEN COMPLETELY RENOVATED</p>

  <div class="frame"></div>
</main>
</body>
</html>
```